SPL Flyer design

we require a flyer design for a new talent convention happening in London. The flyer can be any size as long as it fits into a standard envelope, we would like to produce in full colour and we have a brand logo and web site www.sparkpathlive.co.uk
It would be good if the design tied in with the web site. We are looking for a clean up market design with a bit of fun. Target audience: all ages from 4 to adult so to appeal to parents and children and adults. The images should feature all ages there is a selection on the web site most of which we have as high res versions.
The flyer will be printed, hosted on the web site and emailed to prospects. We would like what the convention is about and the main selling points to be very clear.
we have text for the flyer if it is useful for you to have a copy?
Reason: I have realised that asking for this design in 2 days is a bit unpractical with world wide time lines so I have extended the deadline hope this helps
Please can I have all designs in by the morning of 15th March as I wish to make a decision and proceed immediately. Thank you
Target Market(s)
actors and performers (or parents of children that perform)
Industry/Entity Type
Adult
Requirements
Must have
- email/web and call to action
strong use of colour and images
clean modern feel
our logo

```html
<!DOCTYPE html>
<html lang="en">
<head>
<meta charset="utf-8">
<title>Spark Path Live – Flyer</title>
<link rel="stylesheet" href="https://fonts.googleapis.com/css2?family=Archivo+Black&family=Roboto:ital,wght@0,400;0,700;1,400;1,700&family=Roboto+Condensed:ital,wght@0,700;1,700&display=swap">
<style>
  :root {
    --canvas: #ececec;
    --purple: #7a2aa6;
    --purple-deep: #5e1a8a;
    --violet: #8d3fbe;
    --teal: #2fb7bf;
    --band: #b46ccd;
    --band-dark: #9e52bb;
    --mint: #a3cfc6;
    --ink: #111;
    --white: #fff;
    --night: #0c1416;
  }
  * { box-sizing: border-box; margin: 0; padding: 0; }
  html, body { width: 1200px; height: 856px; overflow: hidden; }
  body {
    background: var(--canvas);
    font-family: "Roboto", Arial, sans-serif;
    position: relative;
  }
  .page {
    position: absolute;
    top: 36px;
    width: 551px;
    height: 778px;
    overflow: hidden;
    box-shadow: 0 2px 6px rgba(0,0,0,.25);
  }
  .abs { position: absolute; }

  /* ---------- Front ---------- */
  .front { left: 41px; background: var(--white); }
  .front-hero {
    left: 0; top: 0; width: 551px; height: 248px;
    background: linear-gradient(160deg, #f4f2f8 0%, #e8e0f1 55%, #d9c9ea 100%);
  }
  .hero-photo {
    left: 10px; top: 10px; width: 270px; height: 238px;
    background: radial-gradient(ellipse at 45% 45%, #b8c49a 0%, #9aa6c4 45%, rgba(220,214,236,0) 75%);
  }
  .brand {
    left: 330px; top: 96px; display: flex; align-items: center; gap: 8px;
    font-weight: 700; font-size: 14px; color: var(--purple-deep);
  }
  .brand-dot { width: 12px; height: 12px; border-radius: 50%; background: var(--purple-deep); }
  .partner {
    left: 400px; top: 124px; display: flex; align-items: center; gap: 6px;
    font-weight: 700; font-size: 11px; color: #1f2a5a; letter-spacing: .5px;
  }
  .partner-sq { width: 10px; height: 10px; background: #1f2a5a; }
  .front-body {
    left: 0; top: 248px; width: 551px; height: 440px;
    background: linear-gradient(180deg, var(--purple) 0%, var(--violet) 28%, #5f7fcf 62%, var(--teal) 100%);
  }
  .front-body::before {
    content: ""; position: absolute; left: 0; top: 0; width: 100%; height: 155px;
    background: linear-gradient(170deg, rgba(255,255,255,.08) 30%, rgba(0,0,0,.08) 70%);
  }
  .title-big {
    font-family: "Archivo Black", "Arial Black", sans-serif;
    color: #f2f0f4; line-height: 1; text-shadow: 0 2px 3px rgba(0,0,0,.35);
  }
  .title-spark { right: 54px; top: 250px; font-size: 84px; letter-spacing: 1px; }
  .title-row { right: 54px; top: 322px; display: flex; align-items: flex-end; gap: 16px; }
  .title-small { font-size: 30px; color: #f2f0f4; font-weight: 400; padding-bottom: 6px; }
  .title-live { font-family: "Roboto Condensed", sans-serif; font-weight: 700; font-size: 70px; line-height: .85; color: #fff; text-shadow: 0 2px 3px rgba(0,0,0,.3); }
  .date { right: 64px; top: 386px; font-family: "Roboto Condensed", sans-serif; font-weight: 700; font-size: 20px; color: #fff; }
  .intro { left: 58px; top: 426px; width: 434px; font-size: 11px; line-height: 14px; color: #fff; }
  .vip-head { left: 58px; top: 520px; width: 420px; font-family: "Roboto Condensed", sans-serif; font-weight: 700; font-size: 14px; line-height: 14px; color: #fff; }
  .perks { left: 93px; top: 564px; list-style: none; font-style: italic; font-size: 11.2px; line-height: 15.8px; color: #fff; }
  .perks li::before { content: "• "; font-style: normal; }
  .cta-band { left: 0; top: 688px; width: 551px; height: 90px; background: linear-gradient(180deg, #eefafa, #fff); text-align: center; }
  .cta-head { margin-top: 18px; font-family: "Roboto Condensed", sans-serif; font-weight: 700; font-size: 19px; color: var(--purple); }
  .cta-text { margin-top: 6px; font-size: 12.5px; line-height: 13.5px; color: var(--ink); }

  /* ---------- Back ---------- */
  .back { left: 611px; background: linear-gradient(180deg, #2e6870 0%, #163238 38%, var(--night) 58%, #070b0c 100%); }
  .back-photo {
    left: 0; top: 0; width: 293px; height: 340px;
    background: radial-gradient(ellipse at 40% 40%, #5f98a0 0%, #2e6870 45%, rgba(22,50,56,0) 80%);
  }
  .mint-strip { left: 517px; top: 0; width: 34px; height: 778px; background: var(--mint); }
  .purple-band { left: 293px; top: 0; width: 224px; height: 778px; background: linear-gradient(160deg, var(--band) 0%, var(--band-dark) 55%, #a75cc4 100%); }
  .polaroid { background: #fff; padding: 8px 8px 26px; box-shadow: 0 2px 6px rgba(0,0,0,.35); }
  .polaroid .shot { width: 100%; height: 100%; }
  .polaroid .tag { position: absolute; left: 0; right: 0; bottom: 4px; text-align: center; font-family: "Roboto Condensed", sans-serif; font-weight: 700; font-size: 15px; color: var(--purple-deep); }
  .pol-acting { left: 292px; top: 24px; width: 146px; height: 158px; transform: rotate(20deg); z-index: 1; }
  .pol-acting .shot { background: linear-gradient(160deg, #d9c4b4, #8a8fa0); }
  .pol-dance { left: 282px; top: 198px; width: 148px; height: 156px; transform: rotate(-13deg); z-index: 2; }
  .pol-dance .shot { background: linear-gradient(160deg, #6a4a3a, #c79a80); }
  .pol-model { left: 382px; top: 124px; width: 144px; height: 164px; transform: rotate(6deg); z-index: 3; }
  .pol-model .shot { background: linear-gradient(170deg, #b4b0b0, #4f4a60); }
  .back-copy { left: 41px; top: 350px; width: 232px; font-size: 10.8px; line-height: 12.3px; color: #fff; }
  .steps { left: 41px; top: 486px; width: 238px; list-style: none; font-style: italic; font-size: 9.8px; line-height: 10px; color: #fff; }
  .steps li { display: flex; gap: 3px; margin-bottom: 6px; }
  .note { left: 41px; width: 236px; font-size: 10px; line-height: 12.2px; color: #fff; }
  .note-vip { top: 626px; }
  .note-agency { top: 681px; }
  .offer { left: 300px; top: 400px; width: 202px; text-align: right; font-family: "Roboto Condensed", sans-serif; font-style: italic; font-weight: 700; font-size: 16px; line-height: 16.5px; color: #fff; }
  .included-bar { left: 282px; top: 496px; width: 245px; height: 25px; background: linear-gradient(180deg, #fff, #cfcfd2); padding: 3px 0 0 24px; font-family: "Roboto Condensed", sans-serif; font-weight: 700; font-size: 17px; color: var(--purple-deep); }
  .included { left: 305px; top: 527px; list-style: none; font-size: 10.3px; line-height: 14.6px; color: #fff; }
  .contact { left: 307px; top: 665px; font-size: 11.5px; line-height: 13.4px; color: #fff; }
  .contact b { font-weight: 700; }
</style>
</head>
<body>

<section class="page front">
  <div class="abs front-hero">
    <div class="abs hero-photo" role="img" aria-label="Photo of a young dancer leaping in a green jacket and pink top"></div>
    <div class="abs brand"><span class="brand-dot"></span>sparkpathlive</div>
    <div class="abs partner"><span class="partner-sq"></span>LANTERN THEATRE</div>
  </div>
  <div class="abs front-body"></div>
  <div class="abs title-big title-spark">SPARK</div>
  <div class="abs title-row">
    <span class="title-small">PATH</span>
    <span class="title-live">LIVE</span>
  </div>
  <div class="abs date">June 21-23 2012</div>
  <p class="abs intro">Spark Path Live (SPL) a unique three day showcase for Actors, Singers, Dancers and Models of all ages. This is an opportunity for YOU to present to and network with industry leaders that can directly influence your career. Come and perform on the Lantern Theatre stage in front of our panel, attend educational seminars and workshops, find an agent, get personal feedback with the chance to be chosen to perform in our Saturday night talent show.</p>
  <h2 class="abs vip-head">VIP panel of CASTING DIRECTORS, MUSIC A&amp;R, AGENTS,<br>MODELING AGENTS and PRODUCERS</h2>
  <ul class="abs perks">
    <li>Gain experience - build networking skills</li>
    <li>Daily call backs plus guaranteed meetings with your choice of VIP</li>
    <li>Guaranteed agency signing</li>
    <li>Limited numbers - online audition to keep quality high</li>
    <li>Saturday night talent show</li>
    <li>Invaluable feed-back</li>
    <li>Amazing value - benefit from our launch special price</li>
  </ul>
  <div class="abs cta-band">
    <h3 class="cta-head">Take action now to secure your place</h3>
    <p class="cta-text">Go to <b>www.sparkpathlive.co.uk</b> and complete<br>the application form <b>mail@sparkpathlive.co.uk</b></p>
  </div>
</section>

<section class="page back">
  <div class="abs back-photo" role="img" aria-label="Photo of an empty folding chair on a spotlit stage"></div>
  <div class="abs purple-band"></div>
  <div class="abs mint-strip"></div>

  <figure class="abs polaroid pol-acting">
    <div class="shot" role="img" aria-label="Photo of a young child for acting"></div>
    <figcaption class="tag">Acting</figcaption>
  </figure>
  <figure class="abs polaroid pol-dance">
    <div class="shot" role="img" aria-label="Photo of a smiling girl for dancing and singing"></div>
    <figcaption class="tag">Dancing &amp; Singing</figcaption>
  </figure>
  <figure class="abs polaroid pol-model">
    <div class="shot" role="img" aria-label="Photo of a young man in a hood for modeling"></div>
    <figcaption class="tag">Modeling</figcaption>
  </figure>

  <p class="abs back-copy">Spark Path Live is an exciting new way for performers and models to take the next step to being discovered. Based on similar events in the US but adapted for Europe this “invitation only” event gives you a “solo” platform in front of a panel of agents, music A&amp;R, casting directors, film directors and producers. You will get personal exposure and maximum networking opportunities. SPL prepares, protects and promotes talent in a safe environment.</p>
  <ol class="abs steps">
    <li><span>1.</span><span>Spread over three full days with daily industry led workshops and a range of talent showcases and modeling</span></li>
    <li><span>2.</span><span>Dance - acting - singing - modeling catwalk and commercial</span></li>
    <li><span>3.</span><span>Take part in as many genres as you wish</span></li>
    <li><span>4.</span><span>Perform on the stage at the Lantern Theatre</span></li>
    <li><span>5.</span><span>Seminars and workshops by leading professionals</span></li>
    <li><span>6.</span><span>Call backs will be given throughout the event</span></li>
  </ol>
  <p class="abs note note-vip">VIP's - we are collating an amazing list of influential people ready to mentor and develop talent. Watch our web site for announcements or sign up for our newsletter to get latest developments</p>
  <p class="abs note note-agency">All entrants will be given the option to sign with Northgate Agency for one year this is a guarantee of representation - options and offers may also be made by agent VIP's at the event - you pick the one that suits you best</p>

  <p class="abs offer">People in the Top 10% of<br>marks will be offered a<br>free return to the event in<br>October 2012</p>
  <h3 class="abs included-bar">Included in price</h3>
  <ul class="abs included">
    <li>Online training how to get the best from SPL</li>
    <li>Online and email mentoring</li>
    <li>All presentations</li>
    <li>Inclusion in Programme</li>
    <li>Picture and c.v. hosted on our site.</li>
    <li>Sponsorship goody bags</li>
    <li>SPL welcome bag and t-shirt</li>
  </ul>
  <p class="abs contact">tel: <b>01632 960415</b><br>web: <b>www.sparkpathlive.co.uk</b><br>mail: <b>mail@sparkpathlive.co.uk</b></p>
</section>

</body>
</html>
```